Property management company looking for modern card design

We at Blue Heron Partners provides property management services for its residential and commercial properties, with expertise in all categories of multifamily, industrial and office projects throughout California.

We need a business card design that is professional and modern designed business card. In our field, clients get hundreds of business cards, we would like our card to stand out.

Please avoid small print.

Target Market(s)

Professionals and high end clients

Industry/Entity Type

Financial Planning

Contact Information for Business Card

Company Name: Blue Heron Partners, Name, email, license #, phone number, website blueheronpartners.com

Font styles to use
Sans Serif

Requirements
Must have
• The card design needs to be adaptable because there is a possibly we will be expanding into different sectors other than real estate. The card design should be focused on financial planning and asset management.
Nice to have
• Modern and simple business card. Eye catching. Non-standard size/shaped cards would be great.
• blueheronpartners.com
Should not have
• Too many bright color or any pictures or shapes of real estate stuff.

```html
<!DOCTYPE html>
<html lang="en">
<head>
<meta charset="utf-8">
<title>Blue Heron Partners – Business Card</title>
<link rel="stylesheet" href="https://fonts.googleapis.com/css2?family=Open+Sans:wght@400;600&family=Raleway:wght@400&display=swap">
<style>
  :root {
    --bg-top: #2b2b2b;
    --bg-bottom: #060606;
    --card: #ffffff;
    --accent: #d7141e;
    --accent-dark: #8e1016;
    --ink: #2e2e2e;
    --rule: #9a9a9a;
  }
  * { margin: 0; padding: 0; box-sizing: border-box; }
  html, body { width: 1200px; height: 900px; overflow: hidden; }
  body {
    position: relative;
    background: linear-gradient(180deg, var(--bg-top) 0%, var(--bg-bottom) 100%);
    font-family: "Open Sans", Arial, sans-serif;
  }
  .card {
    position: absolute;
    top: 306px;
    height: 271px;
    background: var(--card);
    border-radius: 10px;
  }
  .card--front { left: 149px; width: 439px; }
  .card--back { left: 608px; width: 441px; }

  .brand-mark {
    position: absolute;
    left: 44px;
    top: 48px;
    width: 150px;
    text-align: center;
  }
  .brand-mark__dot {
    width: 92px; height: 92px;
    margin: 0 auto 12px;
    border-radius: 50%;
    background: var(--accent-dark);
  }
  .brand-mark__name {
    font-size: 14px;
    font-weight: 600;
    color: var(--accent-dark);
  }

  .contact { position: absolute; left: 239px; top: 70px; color: var(--ink); }
  .contact__name { font-size: 14px; font-weight: 600; color: var(--accent); line-height: 18px; }
  .contact__role { font-size: 12px; line-height: 15px; }
  .contact__license { margin-top: 22px; font-size: 12px; line-height: 16px; }
  .contact__license-label { font-size: 13px; font-weight: 600; color: var(--accent); }
  .contact__list { list-style: none; margin-top: 10px; }
  .contact__item { display: flex; align-items: center; font-size: 12px; line-height: 16px; }
  .contact__icon { width: 9px; height: 9px; margin-right: 7px; fill: var(--accent); }

  .wordmark {
    position: absolute;
    left: 0; right: 0; top: 92px;
    text-align: center;
    font-family: "Raleway", Arial, sans-serif;
    font-size: 38px;
    font-weight: 400;
    color: var(--accent-dark);
    letter-spacing: 0.5px;
  }
  .wordmark-rule {
    position: absolute;
    left: 67px; right: 67px; top: 162px;
    height: 1px;
    background: var(--rule);
  }
</style>
</head>
<body>
  <section class="card card--front">
    <div class="brand-mark">
      <div class="brand-mark__dot"></div>
      <div class="brand-mark__name">Blue Heron Partners</div>
    </div>
    <div class="contact">
      <p class="contact__name">Daniel Reyes</p>
      <p class="contact__role">Managing Director</p>
      <p class="contact__license"><span class="contact__license-label">License:</span> BHP01245</p>
      <ul class="contact__list">
        <li class="contact__item">
          <svg class="contact__icon" viewBox="0 0 10 10"><path d="M2 0.5 L3.6 2.8 L2.7 3.8 C3.3 5.2 4.8 6.7 6.2 7.3 L7.2 6.4 L9.5 8 L8.4 9.5 C4.5 9.2 0.8 5.5 0.5 1.6 Z"/></svg>
          044-987 650 321
        </li>
        <li class="contact__item">
          <svg class="contact__icon" viewBox="0 0 10 10"><path d="M0.5 2 H9.5 V8 H0.5 Z M1 2.4 L5 5.4 L9 2.4" stroke="#fff" stroke-width="0.8"/></svg>
          info@blueheronpartners.com
        </li>
        <li class="contact__item">
          <svg class="contact__icon" viewBox="0 0 10 10"><circle cx="5" cy="5" r="4.5"/></svg>
          www.blueheronpartners.com
        </li>
      </ul>
    </div>
  </section>

  <section class="card card--back">
    <h1 class="wordmark">Blue Heron Partners</h1>
    <div class="wordmark-rule"></div>
  </section>
</body>
</html>
```